"The Wandering Mentor", a Higher Ed blogger, would like a wordpress design

I would like a wordpress design for blogs written by "The Wandering Mentor." that can be easily expanded by me once the initial design is complete.

Here is context which I would like included on the Home/Welcome page: "I started The Wandering Mentor in 2021 to write about the practice of academic advising through the lens of horsemanship. After one year of developing skills as a brand new equestrian, I couldn’t help but notice the similarities between my vocation as an academic advisor and my avocation as a budding equestrian. I hope my musings about my journey in two very different fields will cultivate curiosity, widen your aperture and ignite academic advisors to take their practice to the next level. "

The wordpress will primarily have blogs by myself or guest bloggers writing about academic advising for advisors, but I may widen my audience to include students and families. I'd like to have readers submit questions that I can answer. Depending on interest, I may want to have a section on Horsemanship but that is not truly the focus of this site.

I'd like the feel of the site to be positive, fresh, modern (but not too wild), with the emphasis on Higher Ed/Academic Advising as opposed to equestrian pursuits. I don't want it to feel clunky and blocky like some sites that have to do with education. I'm hoping that readers will have some "aha" moments after reading some of the posts.

I have included my logo files

```html
<!DOCTYPE html>
<html lang="en">
<head>
<meta charset="utf-8">
<title>The Wandering Mentor</title>
<link href="https://fonts.googleapis.com/css2?family=Mulish:wght@400;500;600;700&family=Oswald:wght@500&display=swap" rel="stylesheet">
<style>
:root{
  --bg:#000;
  --panel:#121212;
  --gold:#d9a85b;
  --white:#fff;
  --text:#c9c9c9;
  --muted:#9a9a9a;
  --line:#2c2c2c;
  --input:#7d7d7d;
}
*{box-sizing:border-box;margin:0;padding:0}
html,body{width:1200px;height:3880px;overflow:hidden;background:var(--bg)}
body{position:relative;font-family:"Mulish",sans-serif;color:var(--text)}
h1,h2,h3{font-weight:400}
.abs{position:absolute}
.photo{position:absolute;display:block}
a{color:inherit;text-decoration:none}

/* header */
.brand{left:160px;top:22px;width:170px;height:76px;display:flex;align-items:center;gap:10px}
.brand-dot{width:26px;height:26px;border:2px solid var(--gold);border-radius:50%;flex:none}
.brand-name{color:var(--gold);font-size:17px;font-weight:600;line-height:1.15;letter-spacing:.5px}
.socials{display:flex;gap:8px}
.socials span{width:25px;height:25px;border:1.5px solid var(--gold);border-radius:50%;display:block}
.header-social{left:733px;top:26px}
.search{left:888px;top:26px;width:152px;height:24px;border-bottom:1px solid #777;font-size:13px;color:#bbb;padding-top:2px}
.search svg{position:absolute;right:2px;top:3px}
.nav{display:flex;gap:31px;font-size:14px}
.nav a{color:var(--gold)}
.nav a.current{color:#ddd}
.header-nav{left:578px;top:74px}

/* hero */
.hero{left:0;top:116px;width:1200px;height:526px;background:linear-gradient(180deg,#2f3a26 0%,#3b4a2c 40%,#4c4a32 65%,#3a2e24 100%)}
.hero::after{content:"";position:absolute;inset:0;background:rgba(0,0,0,.45)}
.hero-title{left:0;top:376px;width:1200px;text-align:center;color:var(--white);font-size:42px;font-weight:500;line-height:50px}

/* cards */
.card{position:absolute;background:var(--panel)}
.date{font-size:13px;color:var(--gold);font-weight:600}
.post-title{color:#e6e6e6;font-weight:400}
.excerpt{font-size:12.5px;line-height:22px;color:var(--muted)}
.btn{display:inline-block;border:1.5px solid var(--gold);color:var(--gold);font-size:13px;padding:8px 17px}

.feature-card{left:585px;top:757px;width:453px;height:290px;padding:26px 20px 0 47px}
.feature-card .post-title{font-size:24px;line-height:29px;margin:8px 0 8px}
.feature-card .btn{margin-top:15px}

/* banner ad */
.banner{left:208px;top:1135px;width:784px;height:107px;border:5px solid #8a8a8a;background:#1b1b1b}
.banner-book{left:8px;top:6px;width:105px;height:85px;background:linear-gradient(135deg,#f2f2f2,#d8d8d8)}
.banner-text{left:118px;top:36px;font-family:"Oswald",sans-serif;font-size:24px;color:#eee;letter-spacing:.5px}
.banner-brand{left:640px;top:14px;color:#fff;font-size:22px;font-weight:600}
.banner-cta{left:590px;top:62px;width:175px;height:26px;background:#f39a1f;color:#fff;font-family:"Oswald",sans-serif;font-size:13px;text-align:center;line-height:26px}

/* list posts */
.list-post{left:162px;width:570px;height:195px}
.list-post .photo{left:0;top:0;width:269px;height:195px}
.list-body{position:absolute;left:292px;top:5px;width:270px}
.list-body .post-title{font-size:18px;line-height:23px;margin:6px 0 5px}
.list-body .btn{margin-top:10px}

/* sidebar */
.side-box{left:769px;width:269px;background:var(--panel);padding:24px 16px}
.side-title{font-size:19px;color:#e6e6e6}
.side-rule{width:54px;height:2px;background:var(--gold);margin:9px 0 22px}
.side-text{font-size:12.5px;line-height:19px;color:var(--muted)}
.side-input{margin-top:14px;height:36px;background:var(--input);font-size:11px;color:#e8e8e8;padding:12px 12px}
.side-box .btn{margin-top:12px;padding:6px 12px}
.ad-slot{left:769px;top:1716px;width:269px;height:225px;background:#c9c9c9;overflow:hidden}
.ad-slot span{position:absolute;left:40px;top:96px;font-size:29px;color:#111;transform:rotate(-31deg);transform-origin:center;width:200px;text-align:center}

/* grid posts */
.grid-post{top:1976px;width:270px}
.grid-post .photo{position:relative;width:269px;height:195px}
.grid-post .date{margin-top:24px}
.grid-post .post-title{font-size:18px;line-height:23px;margin:6px 0 5px}
.grid-post .btn{margin-top:10px}

/* pagination */
.pager{left:484px;top:2433px;display:flex;gap:6px;align-items:center}
.pager span{width:20px;height:20px;border:1.5px solid var(--gold);border-radius:3px;font-size:10px;color:var(--gold);display:flex;align-items:center;justify-content:center}
.pager .arrow{width:22px;height:22px}
.pager .gap{border:none;width:22px;font-size:16px;color:#ccc}

/* about */
.section-title{left:0;width:1200px;text-align:center;font-size:24px;font-weight:400;color:#e6e6e6}
.about-card{left:585px;top:2731px;width:453px;height:290px;padding:31px 22px 0 34px}
.about-lead{font-size:16px;line-height:23px;color:#e0e0e0;margin-bottom:14px}

/* newsletter */
.news-title{top:3185px;font-size:26px}
.news-text{left:0;top:3243px;width:1200px;text-align:center;font-size:13.5px;line-height:22px;color:var(--muted)}
.news-input{left:292px;top:3298px;width:482px;height:44px;background:var(--input);font-size:13px;color:#eee;padding:14px 14px}
.news-btn{left:786px;top:3298px;width:121px;height:44px;border:1.5px solid var(--gold);color:var(--gold);font-size:16px;text-align:center;line-height:41px}

/* footer */
.footer-bg{left:0;top:3570px;width:1200px;height:310px;background:#111}
.footer-badge{left:515px;top:3445px;width:170px;height:170px;border-radius:50%;background:#111;display:flex;align-items:center;justify-content:center;text-align:center;color:var(--gold);font-size:16px;font-weight:600;line-height:1.25}
.footer-nav{left:370px;top:3645px}
.footer-rule{left:161px;width:877px;height:1px;background:var(--line)}
.contact{display:flex;align-items:center;gap:16px;top:3732px;font-size:13px;color:#e6e6e6;line-height:21px}
.contact-icon{width:48px;height:48px;border:1.5px solid var(--gold);border-radius:50%;display:flex;align-items:center;justify-content:center;flex:none}
.copyright{left:0;top:3830px;width:1200px;text-align:center;font-size:13px;color:#e6e6e6}
</style>
</head>
<body>

<header>
  <div class="abs brand"><span class="brand-dot"></span><span class="brand-name">The Wandering<br>Mentor</span></div>
  <div class="abs socials header-social" aria-label="Social links"><span></span><span></span><span></span><span></span></div>
  <div class="abs search">Search
    <svg width="14" height="14" viewBox="0 0 14 14" fill="none" stroke="#bbb" stroke-width="1.5"><circle cx="6" cy="6" r="4.5"/><path d="M9.5 9.5L13 13"/></svg>
  </div>
  <nav class="abs nav header-nav"><a class="current">Home</a><a>Academic Topics</a><a>Coaching</a><a>About</a><a>Horsemanship</a></nav>
</header>

<section class="abs hero" role="img" aria-label="Rider clearing a show jump on a chestnut horse in a grassy arena"></section>
<h1 class="abs hero-title">Providing Academic Advising<br>Through The Lens of Horsemanship</h1>

<article>
  <div class="photo" style="left:161px;top:717px;width:476px;height:362px;background:linear-gradient(135deg,#23301c,#6b4a1f 55%,#b06a22)" role="img" aria-label="White horse standing among autumn trees"></div>
  <div class="card feature-card">
    <div class="date">January 29, 2021</div>
    <h2 class="post-title">Lorem Ipsum Dolor Sit Amet, Cons Ctetuer Adipiscing Elit</h2>
    <p class="excerpt">Lorem ipsum dolor sit amet, consectetuer adipiscing elit, sed diam nonummy nibh euismod tincidunt ut laoreet ore magna aliquam erat volutpat. Ut wisi enim ad minim veniam, quis nostrud exerci tation ullamcorper suscipit lobortis nisl ut aliquip ex ea commodo consequat.</p>
    <a class="btn">Read More</a>
  </div>
</article>

<div class="abs banner">
  <div class="abs banner-book" role="img" aria-label="Audiobook cover"></div>
  <div class="abs banner-text">ENJOY BOOKS IN A WHOLE NEW WAY</div>
  <div class="abs banner-brand">Listenwell</div>
  <div class="abs banner-cta">2 FREE AUDIOBOOKS</div>
</div>

<article class="abs list-post" style="top:1303px">
  <div class="photo" style="background:linear-gradient(135deg,#7a8f3a,#a4b45a 50%,#6e5a3a)" role="img" aria-label="Woman kneeling beside a resting horse in a meadow"></div>
  <div class="list-body"><div class="date">January 29, 2021</div><h3 class="post-title">Lorem Ipsum Dolor Sit Met, Cons Ctetuer Adipisci.</h3><p class="excerpt">Lorem ipsum dolor sit amet, ectetuer adipiscing elit, sed diam nonummy nibh euismod tincidunt ut lao.</p><a class="btn">Read More</a></div>
</article>
<article class="abs list-post" style="top:1527px">
  <div class="photo" style="background:linear-gradient(180deg,#9fb3c4,#c8c8c0 55%,#b9ab95)" role="img" aria-label="Rider jumping a grey horse over a fence"></div>
  <div class="list-body"><div class="date">January 29, 2021</div><h3 class="post-title">Lorem Ipsum Dolor Sit Met, Cons Ctetuer Adipisci.</h3><p class="excerpt">Lorem ipsum dolor sit amet, ectetuer adipiscing elit, sed diam nonummy nibh euismod tincidunt ut lao.</p><a class="btn">Read More</a></div>
</article>
<article class="abs list-post" style="top:1747px">
  <div class="photo" style="background:linear-gradient(135deg,#a9b4bd,#e8eaec 50%,#5a6b80)" role="img" aria-label="Colleagues chatting in a bright office"></div>
  <div class="list-body"><div class="date">January 29, 2021</div><h3 class="post-title">Lorem Ipsum Dolor Sit Met, Cons Ctetuer Adipisci.</h3><p class="excerpt">Lorem ipsum dolor sit amet, ectetuer adipiscing elit, sed diam nonummy nibh euismod tincidunt ut lao.</p><a class="btn">Read More</a></div>
</article>

<aside>
  <div class="abs side-box" style="top:1303px;height:221px">
    <div class="side-title">Subscribe To Our Blog</div><div class="side-rule"></div>
    <p class="side-text">Get the latest tips &amp; updates right to your inbox</p>
    <div class="side-input">Enter Your email</div>
    <a class="btn">Subscribe</a>
  </div>
  <div class="abs side-box" style="top:1556px;height:128px">
    <div class="side-title">Follow Us On</div><div class="side-rule" style="margin-bottom:16px"></div>
    <div class="socials"><span></span><span></span><span></span><span></span></div>
  </div>
  <div class="abs ad-slot"><span>Your AD Here</span></div>
</aside>

<article class="abs grid-post" style="left:161px">
  <div class="photo" style="background:linear-gradient(180deg,#7fb0e0,#a7c0d0 40%,#8a8a7a 70%,#c7b79a)" role="img" aria-label="Horse and rider over a jump with mountains behind"></div>
  <div class="date">January 29, 2021</div><h3 class="post-title">Lorem Ipsum Dolor Sit Met, Cons Ctetuer Adipisci.</h3><p class="excerpt">Lorem ipsum dolor sit amet, ectetuer adipiscing elit, sed diam nonummy nibh euismod tincidunt ut lao.</p><a class="btn">Read More</a>
</article>
<article class="abs grid-post" style="left:464px">
  <div class="photo" style="background:linear-gradient(135deg,#dfe6ea,#c9b79a 50%,#e4e4e4)" role="img" aria-label="Students studying together at a table"></div>
  <div class="date">January 29, 2021</div><h3 class="post-title">Lorem Ipsum Dolor Sit Met, Cons Ctetuer Adipisci.</h3><p class="excerpt">Lorem ipsum dolor sit amet, ectetuer adipiscing elit, sed diam nonummy nibh euismod tincidunt ut lao.</p><a class="btn">Read More</a>
</article>
<article class="abs grid-post" style="left:768px">
  <div class="photo" style="background:linear-gradient(180deg,#3f6a2c,#5d8a3c 50%,#b8a88c)" role="img" aria-label="Rider on a chestnut horse in a sand arena"></div>
  <div class="date">January 29, 2021</div><h3 class="post-title">Lorem Ipsum Dolor Sit Met, Cons Ctetuer Adipisci.</h3><p class="excerpt">Lorem ipsum dolor sit amet, ectetuer adipiscing elit, sed diam nonummy nibh euismod tincidunt ut lao.</p><a class="btn">Read More</a>
</article>

<nav class="abs pager" aria-label="Pagination">
  <span class="arrow"><svg width="8" height="10" viewBox="0 0 8 10" fill="none" stroke="#ddd" stroke-width="1.5"><path d="M6 1L2 5l4 4"/></svg></span>
  <span style="margin-left:26px">1</span><span>2</span><span>3</span><span class="gap">…</span><span>8</span>
  <span class="arrow" style="margin-left:4px"><svg width="8" height="10" viewBox="0 0 8 10" fill="none" stroke="#d9a85b" stroke-width="1.5"><path d="M2 1l4 4-4 4"/></svg></span>
</nav>

<section>
  <h2 class="abs section-title" style="top:2607px">About The Wandering Mentor</h2>
  <div class="photo" style="left:161px;top:2690px;width:476px;height:363px;background:linear-gradient(135deg,#5b6a3a,#7a6a4a 45%,#3a2a20)" role="img" aria-label="Clara Bennett, The Wandering Mentor, embracing a paint horse"></div>
  <div class="card about-card">
    <p class="about-lead">I started The Wandering Mentor in 2021 to write about the practice of academic advising through the lens of horsemanship</p>
    <p class="excerpt">After one year of developing skills as a brand new equestrian, I couldn’t help but notice the similarities between my vocation as an academic advisor and my avocation as a budding equestrian. I hope my musings about my journey in two very different fields will cultivate curiosity, widen your aperture and ignite academic advisors to take their practice to the next level.</p>
  </div>
</section>

<section>
  <h2 class="abs section-title news-title">Newsletter Sign Up</h2>
  <p class="abs news-text">Want to keep up to date with all our latest news and information?<br>Enter your email below to be added to our mailing list.</p>
  <div class="abs news-input">Enter your email address</div>
  <div class="abs news-btn">Subscribe</div>
</section>

<footer>
  <div class="abs footer-bg"></div>
  <svg class="abs" style="left:0;top:3560px" width="1200" height="60" viewBox="0 0 1200 60" aria-hidden="true">
    <path d="M0 55Q80 14 380 10H820Q1120 14 1200 55V0H0z" fill="#000"/>
    <path d="M0 55Q80 14 380 10H820Q1120 14 1200 55" fill="none" stroke="#d9a85b" stroke-width="2.5"/>
  </svg>
  <div class="abs footer-badge">The Wandering<br>Mentor</div>
  <nav class="abs nav footer-nav"><a class="current">Home</a><a>Academic Topics</a><a>Coaching</a><a>About</a><a>Horsemanship</a></nav>
  <div class="abs footer-rule" style="top:3685px"></div>
  <div class="abs contact" style="left:185px">
    <span class="contact-icon"><svg width="20" height="20" viewBox="0 0 24 24" fill="none" stroke="#d9a85b" stroke-width="1.6"><path d="M5 3h4l2 5-2.5 1.5a11 11 0 006 6L16 13l5 2v4a2 2 0 01-2 2A16 16 0 013 5a2 2 0 012-2z"/></svg></span>
    <div>PHONE<br>&nbsp;123-456-7890</div>
  </div>
  <div class="abs contact" style="left:430px">
    <span class="contact-icon"><svg width="20" height="20" viewBox="0 0 24 24" fill="none" stroke="#d9a85b" stroke-width="1.6"><path d="M12 22s7-7 7-12a7 7 0 00-14 0c0 5 7 12 7 12z"/><circle cx="12" cy="10" r="2.5"/></svg></span>
    <div>Lorem ipsum dolor sit amet, ectetuer<br>adipiscing elit, sed diam nonu.</div>
  </div>
  <div class="abs contact" style="left:817px">
    <span class="contact-icon"><svg width="20" height="20" viewBox="0 0 24 24" fill="none" stroke="#d9a85b" stroke-width="1.6"><rect x="3" y="6" width="18" height="13" rx="1"/><path d="M3 7l9 7 9-7"/></svg></span>
    <div>EMAIL<br>info@wanderingmentor.example</div>
  </div>
  <div class="abs footer-rule" style="top:3805px"></div>
  <p class="abs copyright">Copyright © 2021 The Wandering Mentor. All Rights Reserved.</p>
</footer>

</body>
</html>
```